Business card design for new, innovative company - BluePlinth

We are a new company looking for a business card design that is fun, different and quirky. Must use corporate colour green - CMYK C:55, M:0, Y:100, K:0, and corporate colour grey - C:0, M:0, Y: 0, K:70.

We have developed the first real time data application, in which people are able to profile the data of their existing customers in order to pull out more good fit clients to direct their marketing activities at.

Industry/Entity Type

Marketing

Requirements
Must have
• Logo, name, title, telephone number, fax number, email, website, address

```html
<!DOCTYPE html>
<html lang="en">
<head>
<meta charset="utf-8">
<title>BluePlinth Business Card</title>
<link href="https://fonts.googleapis.com/css2?family=Didact+Gothic&family=Questrial&display=swap" rel="stylesheet">
<style>
  :root {
    --brand-green: #7ac143;
    --brand-green-light: #9ad85e;
    --brand-grey: #6d6e71;
    --band-white: #f7f7f7;
    --ink-white: #ffffff;
    --backdrop: #e9e9e6;
  }
  * { box-sizing: border-box; margin: 0; padding: 0; }
  html, body {
    width: 1200px; height: 576px; overflow: hidden;
    background: var(--backdrop);
    font-family: "Didact Gothic", "Questrial", sans-serif;
  }
  .canvas {
    position: relative; width: 1200px; height: 576px;
    display: flex; align-items: center; justify-content: center; gap: 60px;
  }
  .card {
    position: relative; width: 520px; height: 330px;
    border-radius: 22px; overflow: hidden;
    background: linear-gradient(160deg, var(--brand-green-light) 0%, var(--brand-green) 70%);
    box-shadow: 0 10px 28px rgba(0,0,0,0.18);
  }
  .band {
    position: absolute; left: 0; right: 0; top: 26px; height: 92px;
    background: var(--band-white);
    display: flex; align-items: center;
  }
  .wordmark {
    display: flex; align-items: center; gap: 12px;
    font-family: "Didact Gothic", sans-serif;
    font-size: 58px; line-height: 1; letter-spacing: -1px;
    color: var(--brand-grey);
  }
  .wordmark-square {
    width: 26px; height: 26px; background: var(--brand-green);
  }
  .card-back .band { padding-left: 56px; }
  .card-front .band { justify-content: flex-end; padding-right: 34px; }
  .back-website {
    position: absolute; right: 34px; bottom: 34px;
    color: var(--ink-white); font-size: 17px; font-weight: bold;
    font-family: "Questrial", sans-serif; letter-spacing: 0.3px;
  }
  .holder {
    position: absolute; left: 30px; top: 146px;
    color: var(--ink-white); font-size: 20px;
  }
  .contacts {
    position: absolute; left: 262px; top: 146px; list-style: none;
    color: var(--ink-white); font-size: 13.5px; line-height: 1.35;
  }
  .contacts li { display: flex; align-items: flex-start; gap: 8px; margin-bottom: 2px; }
  .contacts svg { flex: none; width: 13px; height: 13px; margin-top: 3px; }
  .contacts .web { font-weight: bold; }
</style>
</head>
<body>
<main class="canvas">

  <section class="card card-back" aria-label="Card back">
    <div class="band">
      <div class="wordmark"><span class="wordmark-square"></span>BluePlinth</div>
    </div>
    <p class="back-website">www.blueplinth.com</p>
  </section>

  <section class="card card-front" aria-label="Card front">
    <div class="band">
      <div class="wordmark"><span class="wordmark-square"></span>BluePlinth</div>
    </div>
    <p class="holder">Jenna Collins | CEO</p>
    <ul class="contacts">
      <li>
        <svg viewBox="0 0 16 16" aria-hidden="true"><path d="M8 1a5 5 0 0 0-5 5c0 4 5 9 5 9s5-5 5-9a5 5 0 0 0-5-5zm0 7a2 2 0 1 1 0-4 2 2 0 0 1 0 4z" fill="#fff"/></svg>
        <span>22 Fenmoor Road, Ely,<br>Cambridgeshire, CB7 4XZ</span>
      </li>
      <li>
        <svg viewBox="0 0 16 16" aria-hidden="true"><rect x="4" y="1" width="8" height="14" rx="1.5" fill="#fff"/><rect x="5.5" y="3" width="5" height="8" fill="var(--brand-green)"/></svg>
        <span>07700900412</span>
      </li>
      <li>
        <svg viewBox="0 0 16 16" aria-hidden="true"><rect x="1" y="5" width="14" height="10" rx="1.5" fill="#fff"/><path d="M3 6V3h10v3" stroke="#fff" stroke-width="2" fill="none"/></svg>
        <span>01632 960735</span>
      </li>
      <li>
        <svg viewBox="0 0 16 16" aria-hidden="true"><rect x="1" y="3" width="14" height="10" rx="1" fill="#fff"/><path d="M1.5 3.5 8 9l6.5-5.5" stroke="var(--brand-green)" stroke-width="1.4" fill="none"/></svg>
        <span>jenna.collins@plinthdistribution.com</span>
      </li>
      <li>
        <svg viewBox="0 0 16 16" aria-hidden="true"><circle cx="8" cy="8" r="7" fill="#fff"/><path d="M1 8h14M8 1c-3 3-3 11 0 14M8 1c3 3 3 11 0 14" stroke="var(--brand-green)" stroke-width="1" fill="none"/></svg>
        <span class="web">www.blueplinth.com</span>
      </li>
    </ul>
  </section>

</main>
</body>
</html>
```